Sun Path & Clear Way
Use same font as used in my logo
Marla Tenbeck
48207 hwy 19 north dalworth, ar 71482
mltenbeck@mailvox.example
Please change the color of the logo. i will send the color code. Also need changes to letterhead, envelope & card. need asap. thanks.

```html
<!DOCTYPE html>
<html lang="en">
<head>
<meta charset="utf-8">
<title>Sun Path &amp; Clear Way — Stationery</title>
<link href="https://fonts.googleapis.com/css2?family=Patrick+Hand&family=Open+Sans:wght@400;600;700&display=swap" rel="stylesheet">
<style>
:root{
  --bg:#e9e4df;
  --paper:#ffffff;
  --peach:#f5a57e;
  --peach-light:#fbd3bf;
  --brown:#5b3426;
  --ink:#3a2a24;
  --shadow:rgba(40,25,15,.22);
}
*{margin:0;padding:0;box-sizing:border-box}
html,body{width:1200px;height:782px;overflow:hidden}
body{background:var(--bg);position:relative;font-family:"Open Sans",sans-serif;color:var(--ink)}
.sheet{position:absolute;background:var(--paper);box-shadow:0 3px 10px var(--shadow)}
.brand{display:flex;align-items:center;gap:8px}
.brand-dot{width:30px;height:30px;border-radius:50%;background:var(--peach);flex:none}
.brand-name{font-family:"Patrick Hand",cursive;color:var(--brown);font-size:22px;line-height:1;white-space:nowrap}
.tagline{font-size:7px;letter-spacing:2.5px;color:var(--peach);text-transform:uppercase;white-space:nowrap}
.rule{position:absolute;height:3px;background:var(--peach)}
.contact{font-size:8.5px;color:var(--ink);white-space:nowrap}
.contact b{font-weight:700}
.sep{color:var(--peach);margin:0 8px}
.signer-name{font-family:"Patrick Hand",cursive;font-size:22px;color:var(--brown);line-height:1}
.signer-role{font-size:9px;font-weight:600;letter-spacing:1px;color:var(--ink);text-transform:uppercase}

/* letterhead */
.letterhead{left:65px;top:48px;width:468px;height:629px}
.letterhead .brand{position:absolute;left:22px;top:26px}
.letterhead .tagline{position:absolute;left:60px;top:64px}
.letterhead .signer{position:absolute;right:24px;top:28px;text-align:right}
.letterhead .rule.top{left:20px;right:20px;top:80px}
.letterhead .contact{position:absolute;left:0;right:0;top:574px;text-align:center;line-height:1.9}
.letterhead .rule.bottom{left:20px;right:20px;top:608px}

/* business card */
.card{left:622px;top:60px;width:312px;height:185px;border-radius:10px}
.card .brand{position:absolute;left:0;right:0;top:22px;justify-content:center}
.card .brand-dot{width:26px;height:26px}
.card .brand-name{font-size:20px}
.card .tagline{position:absolute;left:0;right:0;top:56px;text-align:center}
.card .person{position:absolute;left:0;right:0;top:78px;text-align:center}
.card .person .signer-name{font-family:"Open Sans",sans-serif;font-size:18px}
.card .rule{left:22px;right:22px;top:128px}
.card .contact{position:absolute;left:0;right:0;top:138px;text-align:center;font-size:7.5px;line-height:1.7}

/* envelope back */
.envelope-back{left:540px;top:307px;width:598px;height:322px;overflow:hidden}
.envelope-back svg{position:absolute;left:0;top:0}
.flap-text{position:absolute;left:180px;top:16px;color:#fff;font-size:12px;line-height:1.5}
.flap-text span{display:block;padding-left:40px}

/* envelope front */
.envelope-front{left:566px;top:413px;width:572px;height:321px}
.envelope-front .brand{position:absolute;left:20px;top:24px}
.envelope-front .rule{left:20px;right:22px;top:64px}
.envelope-front .tagline{position:absolute;left:58px;top:74px}
.envelope-front .return{position:absolute;right:24px;top:20px;text-align:right;font-size:8.5px;line-height:1.5}
</style>
</head>
<body>

<section class="sheet letterhead" aria-label="Letterhead">
  <div class="brand"><span class="brand-dot"></span><span class="brand-name">Sun Path &amp; Clear Way</span></div>
  <p class="tagline">Share with others</p>
  <div class="signer">
    <p class="signer-name">marla tenbeck</p>
    <p class="signer-role">Director</p>
  </div>
  <div class="rule top"></div>
  <p class="contact"><b>Address</b> 48207 hwy 19 north dalworth, ar 71482<br><b>Email</b> mltenbeck@mailvox.example<span class="sep">|</span><b>Phone</b> 479-555-0163</p>
  <div class="rule bottom"></div>
</section>

<section class="sheet card" aria-label="Business card">
  <div class="brand"><span class="brand-dot"></span><span class="brand-name">Sun Path &amp; Clear Way</span></div>
  <p class="tagline">Share with others</p>
  <div class="person">
    <p class="signer-name">Marla Tenbeck</p>
    <p class="signer-role">Director</p>
  </div>
  <div class="rule"></div>
  <p class="contact"><b>Address</b> 48207 hwy 19 north dalworth, ar 71482<br><b>Phone</b> 479-555-0163<span class="sep">|</span><b>Email</b> mltenbeck@mailvox.example</p>
</section>

<section class="sheet envelope-back" aria-label="Envelope back">
  <svg width="598" height="322" viewBox="0 0 598 322">
    <polygon points="0,0 598,0 598,12 552,90 0,90" fill="var(--peach)"/>
    <polygon points="0,90 552,90 598,12 598,24 558,96 0,96" fill="var(--peach-light)"/>
  </svg>
  <p class="flap-text">Providing food<span>For hunger</span></p>
</section>

<section class="sheet envelope-front" aria-label="Envelope front">
  <div class="brand"><span class="brand-dot"></span><span class="brand-name">Sun Path &amp; Clear Way</span></div>
  <div class="rule"></div>
  <p class="tagline">Share with others</p>
  <p class="return">48207 hwy 19 north<br>dalworth, ar 71482</p>
</section>

</body>
</html>
```